Personal Motivational Quote Poster Design

I would like to create a poster with some of my favorite quotes to hang in my office. I did similar projects in 2012 and 2014. I've uploaded the winning designs so you can get a better idea of what I'm looking for. I will provide feedback on your design within 24 hours of receiving it.

The poster must contain the following quotes:

“What the pupil must learn, if he learns anything at all, is that the world will do most of the work for you, provided you cooperate with it by identifying how it really works and aligning with those realities. If we do not let the world teach us, it teaches us a lesson.” - Walter Brindley

“I tackle every big new problem by asking two questions: Who has dealt with this problem well? And what can we learn from them?” - Hal Porter

“If we can really understand the problem, the answer will come out of it, because the answer is not separate from the problem.” - Ravel Ondashanti

“Success is nothing more than a few simple disciplines, practiced every day; while failure is simply a few errors in judgment, repeated every day. It is the accumulative weight of our disciplines and our judgments that leads us to either fortune or failure.” - Ned Calve

“Inaction breeds doubt and fear. Action breeds confidence and courage.” - Rex Halloway

“What’s the one thing you can do, such that by doing it, everything else will be easier or unnecessary?” - Lyle Danvers

Requirements
Must have
• The poster will be 24" high x 36" long and printed on canvas, so the image you create needs to have a resolution of at least 2700 x 3900.
Nice to have
• I don't have an exact vision for how the poster should look, so I am totally open to you using your creativity to develop, arrange and present the content as you'd like.

That said, I would like an image (photo or posterized image) of the person being quoted along with each quote. I do not have specific images that I would like you to use, so you will need to find the images on your own.

The images don't need to be perfect... I am more interested in the poster relating the essence of the quotes and the people being quoted than I am in perfect photographic images of the people being quoted.

```html
<!DOCTYPE html>
<html lang="en">
<head>
<meta charset="utf-8">
<title>Quotes Poster</title>
<link rel="stylesheet" href="https://fonts.googleapis.com/css2?family=Satisfy&display=swap">
<style>
  :root {
    --frame: #000000;
    --ground: #2c416a;
    --ground-light: #34497a;
    --band: #05070c;
    --red: #e8524f;
    --cream: #f7ecc6;
    --blue: #6f9be8;
    --rose: #cf5b6c;
    --lavender: #8f8ee6;
    --portrait-red: #e5524e;
    --portrait-blue: #5a86d8;
    --portrait-navy: #23386a;
  }
  * { margin: 0; padding: 0; box-sizing: border-box; }
  html, body { width: 831px; height: 1200px; overflow: hidden; background: var(--frame); }
  .poster {
    position: relative;
    width: 831px;
    height: 1200px;
    background: var(--frame);
    overflow: hidden;
  }
  .panel {
    position: absolute;
    left: 47px;
    top: 0;
    width: 750px;
    height: 1200px;
    background: radial-gradient(ellipse at 50% 40%, var(--ground-light), var(--ground) 70%);
    overflow: hidden;
  }
  .bands { position: absolute; left: 0; top: 0; }
  .portrait {
    position: absolute;
    border-radius: 45% 45% 30% 30%;
  }
  .portrait--warm { background: radial-gradient(ellipse at 50% 40%, var(--portrait-red) 0%, var(--portrait-blue) 60%, var(--portrait-navy) 100%); }
  .portrait--pale { background: radial-gradient(ellipse at 50% 40%, var(--cream) 0%, var(--portrait-red) 50%, var(--portrait-navy) 100%); }
  .quote {
    position: absolute;
    font-family: "Satisfy", cursive;
    font-size: 21px;
    line-height: 36.5px;
    text-align: center;
    white-space: nowrap;
    transform: translateX(-50%);
  }
  .quote--red { color: var(--red); }
  .quote--cream { color: var(--cream); }
  .quote--blue { color: var(--blue); }
  .quote--rose { color: var(--rose); }
  .quote--lavender { color: var(--lavender); }
</style>
</head>
<body>
<main class="poster">
  <section class="panel">
    <svg class="bands" width="750" height="1200" viewBox="0 0 750 1200" aria-hidden="true">
      <defs>
        <filter id="soft-edge" x="-10%" y="-30%" width="120%" height="160%">
          <feGaussianBlur stdDeviation="6"/>
        </filter>
      </defs>
      <polygon points="0,300 750,178 750,262 0,372" fill="var(--band)" filter="url(#soft-edge)"/>
      <polygon points="0,775 750,668 750,748 0,832" fill="var(--band)" filter="url(#soft-edge)"/>
    </svg>

    <div class="portrait portrait--warm" style="left:36px;top:52px;width:157px;height:164px" role="img" aria-label="Posterized portrait of Lyle Danvers"></div>
    <div class="portrait portrait--pale" style="left:599px;top:193px;width:114px;height:166px" role="img" aria-label="Posterized portrait of Ravel Ondashanti"></div>
    <div class="portrait portrait--warm" style="left:34px;top:419px;width:151px;height:175px" role="img" aria-label="Posterized portrait of Ned Calve"></div>
    <div class="portrait portrait--warm" style="left:596px;top:614px;width:128px;height:183px" role="img" aria-label="Posterized portrait of Hal Porter"></div>
    <div class="portrait portrait--pale" style="left:31px;top:778px;width:138px;height:190px" role="img" aria-label="Posterized portrait of Rex Halloway"></div>
    <div class="portrait portrait--pale" style="left:580px;top:929px;width:162px;height:180px" role="img" aria-label="Posterized portrait of Walter Brindley"></div>

    <p class="quote quote--red" style="left:440px;top:78px">“What’s the one thing you can do, such<br>that by doing it, everything else will be<br>easier or unnecessary?”</p>

    <p class="quote quote--cream" style="left:320px;top:245px">“If we can really understand the problem, the<br>answer will come out of it, because the answer<br>is not separate from the problem.”</p>

    <p class="quote quote--blue" style="left:450px;top:401px">“Success is nothing more than a few simple<br>disciplines, practiced every day; while failure is<br>simply a few errors in judgment, repeated every<br>day. It is the accumulative weight of our disciplines<br>and our judgments that leads us to either fortune or<br>failure.”</p>

    <p class="quote quote--rose" style="left:325px;top:633px">“I tackle every big new problem by asking two<br>questions: Who has dealt with this problem well?<br>And what can we learn from them?”</p>

    <p class="quote quote--cream" style="left:437px;top:823px">“Inaction breeds doubt and fear. Action breeds<br>confidence and courage.”</p>

    <p class="quote quote--lavender" style="left:328px;top:961px">“What the pupil must learn, if he learns anything at all,<br>is that the world will do most of the work for you,<br>provided you cooperate with it by identifying how it<br>really works and aligning with those realities. If we do<br>not let the world teach us, it teaches us a lesson.”</p>
  </section>
</main>
</body>
</html>
```